Business card for Mortgage broker business

I have already had the logo designed and am needing a great looking business card. My business focus is on servicing clients who may not be able to obtain finance through traditional lenders due to bad credit, short term employment or they just don't fit the banks profile. It needs to be professional, trust worthy but also have a caring fell about it.
I have provided files showing the green and black logo, the white logo(on white background so the file looks blank) and also a file with the white logo with a background of leaves that was made up which will probably be used for a website header.

Industry/Entity Type

Finance

Contact Information for Business Card

Marcus Dalby
Managing Director, Accredited Finance Broker(AFB)
Po Box 817, Pakenham VIC 3810
marcus@kestrelfunding.com.au
www.kestrelfunding.com.au
0438 216 507

Requirements
Nice to have
• I have added a picture of myself as I would like to see some designs with the pic in it, but I'm not sure if I want it on there with the logo's or just the logo's

```html
<!DOCTYPE html>
<html lang="en">
<head>
<meta charset="utf-8">
<title>Kestrel Funding — Business Card</title>
<link rel="stylesheet" href="https://fonts.googleapis.com/css2?family=Arimo:wght@400;700&display=swap">
<style>
  :root {
    --backdrop: #3a322e;
    --card: #1b1b1c;
    --card-edge: #111112;
    --brand-green: #1f8a45;
    --ink-white: #f2f2f2;
    --ink-soft: #d9d9d9;
    --spot-grey: #5f6062;
    --divider: #8a8a8a;
  }
  * { margin: 0; padding: 0; box-sizing: border-box; }
  html, body {
    width: 1200px; height: 864px; overflow: hidden;
    background: var(--backdrop);
    font-family: "Arimo", Arial, sans-serif;
  }
  .canvas { position: relative; width: 1200px; height: 864px; }
  .card {
    position: absolute; width: 600px; height: 343px;
    background: var(--card);
    border: 1px solid var(--card-edge);
    box-shadow: 0 10px 30px rgba(0,0,0,0.35);
  }
  .card-back { left: 50px; top: 60px; }
  .card-front { left: 550px; top: 460px; }

  /* back */
  .back-brand {
    position: absolute; left: 70px; top: 110px;
    font-size: 46px; font-weight: 700; color: var(--spot-grey);
    letter-spacing: 1px;
  }
  .back-web {
    position: absolute; left: 72px; top: 190px;
    font-size: 15px; color: var(--spot-grey); letter-spacing: 4px;
  }

  /* front */
  .front-brand {
    position: absolute; left: 40px; top: 140px;
    font-size: 30px; font-weight: 700; color: var(--brand-green);
  }
  .front-divider {
    position: absolute; left: 300px; top: 40px; width: 1px; height: 265px;
    background: linear-gradient(to bottom, transparent, var(--divider) 20%, var(--divider) 80%, transparent);
  }
  .details { position: absolute; left: 322px; top: 46px; color: var(--ink-white); }
  .details-name { font-size: 20px; color: var(--brand-green); line-height: 24px; }
  .details-title { font-size: 17px; line-height: 22px; margin-bottom: 10px; }
  .details-address { font-size: 14px; line-height: 19px; color: var(--ink-soft); margin-bottom: 10px; }
  .contact-list { list-style: none; }
  .contact-item {
    display: flex; align-items: center; gap: 10px;
    font-size: 14px; line-height: 22px; color: var(--ink-soft);
  }
  .contact-icon { width: 13px; height: 13px; fill: var(--brand-green); flex: none; }
</style>
</head>
<body>
<div class="canvas">

  <section class="card card-back" aria-label="Business card back">
    <div class="back-brand">Kestrel Funding</div>
    <div class="back-web">www.kestrelfunding.com.au</div>
  </section>

  <section class="card card-front" aria-label="Business card front">
    <div class="front-brand">Kestrel Funding</div>
    <div class="front-divider"></div>
    <div class="details">
      <div class="details-name">Marcus Dalby</div>
      <div class="details-title">President</div>
      <div class="details-address">Po Box 817<br>Pakenham VIC 3810</div>
      <ul class="contact-list">
        <li class="contact-item">
          <svg class="contact-icon" viewBox="0 0 16 16"><path d="M3 1h3l1.5 4-2 1.2a9 9 0 0 0 4.3 4.3L11 8.5l4 1.5v3a2 2 0 0 1-2 2C6.4 15 1 9.6 1 3a2 2 0 0 1 2-2z"/></svg>
          0438 216 507
        </li>
        <li class="contact-item">
          <svg class="contact-icon" viewBox="0 0 16 16"><path d="M4 0h8a1 1 0 0 1 1 1v14a1 1 0 0 1-1 1H4a1 1 0 0 1-1-1V1a1 1 0 0 1 1-1zm1 2v10h6V2zm3 11a1 1 0 1 0 0 2 1 1 0 0 0 0-2z"/></svg>
          0391 624 870
        </li>
        <li class="contact-item">
          <svg class="contact-icon" viewBox="0 0 16 16"><path d="M4 1h8v4H4zM1 6h14v7h-3v2H4v-2H1zm4 5v3h6v-3z"/></svg>
          0391 624 871
        </li>
        <li class="contact-item">
          <svg class="contact-icon" viewBox="0 0 16 16"><path d="M1 3h14v10H1zm1.5 1.5L8 9l5.5-4.5V4h-11z"/></svg>
          marcus@kestrelfunding.com.au
        </li>
        <li class="contact-item">
          <svg class="contact-icon" viewBox="0 0 16 16"><path d="M8 1a7 7 0 1 0 0 14A7 7 0 0 0 8 1zm0 1.5c.8 0 1.8 1.7 2 4.5H6c.2-2.8 1.2-4.5 2-4.5zM2.6 7h2c.1-1.6.5-3 1-4A5.5 5.5 0 0 0 2.6 7zm8.8 0h2a5.5 5.5 0 0 0-3-4c.5 1 .9 2.4 1 4zM2.6 9a5.5 5.5 0 0 0 3 4c-.5-1-.9-2.4-1-4zM6 9c.2 2.8 1.2 4.5 2 4.5s1.8-1.7 2-4.5zm5.4 0c-.1 1.6-.5 3-1 4a5.5 5.5 0 0 0 3-4z"/></svg>
          www.kestrelfunding.com.au
        </li>
      </ul>
    </div>
  </section>

</div>
</body>
</html>
```